Startup of Management Company looking for Designers!

I am looking for an upscale website. Veltrona will focus on Real Estate, Wealth Management, and Consulting,

Target Market(s)

investors, sellers of real estate, people looking to have their real estate management.
companies looking for consulting services

Number of Pages Required

5+ page

Font styles to use
Sans Serif

Requirements
Must have
• pictures, real.

```html
<!DOCTYPE html>
<html lang="en">
<head>
<meta charset="utf-8">
<title>Veltrona — Real Estate, Wealth Management &amp; Consulting</title>
<link href="https://fonts.googleapis.com/css2?family=Cinzel:wght@600;700&family=Roboto:wght@400;500;700&display=swap" rel="stylesheet">
<style>
:root{
  --primary:#0b5480;
  --primary-deep:#0a4a72;
  --hero-box:rgba(22,94,132,.88);
  --ink:#1a1a1a;
  --text:#555;
  --muted:#777;
  --field:#efefef;
  --field-line:#ddd;
  --quote-mark:#8fb3ca;
  --white:#fff;
}
*{box-sizing:border-box;margin:0;padding:0}
html,body{width:1200px;height:3468px;overflow:hidden;background:var(--white)}
body{font-family:'Roboto',Arial,sans-serif;color:var(--ink);position:relative}
.abs{position:absolute}
.serif{font-family:'Cinzel',Georgia,serif;font-weight:700}

/* header */
.site-header{position:absolute;left:0;top:0;width:1200px;height:106px}
.brand{left:110px;top:40px;font-size:27px;letter-spacing:.5px;color:#111}
.nav{left:389px;top:42px;display:flex;gap:27px;font-size:15px;font-weight:500;color:#222}
.nav .active{color:var(--primary)}
.login{left:987px;top:34px;width:101px;height:38px;border-radius:19px;background:var(--primary);color:#fff;font-size:15px;font-weight:500;display:flex;align-items:center;justify-content:center;gap:6px}

/* hero */
.hero{left:0;top:106px;width:1200px;height:612px;background:linear-gradient(180deg,#3f8fd4 0%,#8bbce6 45%,#c9d8e4 62%,#7d8a94 80%,#4a6f88 100%)}
.call{left:890px;top:106px;width:198px;height:48px;background:var(--primary-deep);color:#fff;font-size:15px;font-weight:500;display:flex;align-items:center;justify-content:center;gap:8px}
.hero-box{left:112px;top:500px;width:358px;height:296px;background:var(--hero-box);color:#fff;text-align:center}
.hero-box h1{font-size:43px;margin-top:50px;letter-spacing:1px}
.hero-box p{font-size:15px;font-weight:500;line-height:21px;margin:6px 30px 0}
.btn-white{display:inline-flex;align-items:center;justify-content:center;gap:7px;background:#fff;color:var(--primary);border-radius:22px;font-weight:700;font-size:14px}
.hero-box .btn-white{position:absolute;left:98px;top:194px;width:162px;height:42px;font-size:15px}

.section-title{width:1200px;text-align:center;font-size:48px;letter-spacing:1px;color:#111}

/* services */
.card{width:310px;text-align:center}
.card .photo{height:241px;background:linear-gradient(135deg,#d9d4cc,#a89f94 60%,#6f7b86)}
.card h3{font-size:19px;font-weight:500;margin-top:21px}
.card p{font-size:14.5px;color:var(--text);line-height:24px;margin-top:10px}
.btn-blue{display:inline-flex;align-items:center;justify-content:center;gap:7px;background:var(--primary);color:#fff;border-radius:20px;font-weight:700;font-size:14px;width:152px;height:40px;margin-top:18px}

/* about */
.about{left:0;top:1532px;width:1200px;height:435px}
.about-panel{left:0;top:0;width:621px;height:435px;background:var(--primary)}
.about-photo{left:621px;top:0;width:579px;height:435px;background:linear-gradient(135deg,#8a8f88,#c5c2b4 45%,#5c6670)}
.about h2{left:112px;top:56px;font-size:48px;color:#fff;letter-spacing:1px}
.about p{left:112px;width:470px;color:#fff;font-size:14.5px;line-height:24px}
.about .btn-white{left:112px;top:312px;width:168px;height:42px;position:absolute}

/* why */
.why-col{width:310px;text-align:center}
.why-col h4{font-size:17px;font-weight:500;margin-top:20px}
.why-col p{font-size:14.5px;color:var(--muted);line-height:24px;margin-top:12px}

/* clients */
.clients{left:0;top:2439px;width:1200px;height:390px;background:linear-gradient(180deg,#0d5783,#0b5079)}
.clients h2{top:52px;font-size:42px;color:#fff}
.quote{width:320px;text-align:center;color:#fff}
.quote .marks{display:block;margin:0 auto;height:40px}
.quote p{font-size:14.5px;line-height:26px;margin-top:12px}
.quote strong{display:block;font-size:16.5px;font-weight:700;margin-top:14px}

/* contact */
.contact h3{font-size:21px;font-weight:500;color:#333}
.detail{font-size:15px;color:#555;line-height:24px;display:flex;gap:14px}
.map{left:112px;top:3110px;width:390px;height:155px;background:linear-gradient(135deg,#d6d6d6,#bdbdbd 50%,#cfcfcf)}
.field{background:var(--field);border:1px solid var(--field-line);font-size:12px;color:#666;display:flex;align-items:center;gap:6px;padding-left:16px}
.field svg{flex:none}
.submit{left:562px;top:3297px;width:113px;height:42px;background:var(--primary);color:#fff;font-size:15px;font-weight:700;display:flex;align-items:center;justify-content:center}

/* footer */
.site-footer{left:0;top:3419px;width:1200px;height:49px;background:var(--primary);color:#fff;font-size:15px}
.site-footer .legal{position:absolute;left:112px;top:15px}
.social{position:absolute;top:12px;width:25px;height:25px;border:1.5px solid #fff;border-radius:50%}
</style>
</head>
<body>

<header class="site-header">
  <div class="abs brand serif">VELTRONA</div>
  <nav class="abs nav"><span class="active">Home</span><span>About</span><span>Real Estate</span><span>Wealth Management</span><span>Consulting</span><span>Contact</span></nav>
  <div class="abs login"><svg width="11" height="13" viewBox="0 0 11 13"><rect x="1" y="5.5" width="9" height="7" rx="1" fill="#fff"/><path d="M3 5.5V4a2.5 2.5 0 0 1 5 0v1.5" stroke="#fff" stroke-width="1.6" fill="none"/></svg>Login</div>
</header>

<div class="abs hero" role="img" aria-label="City skyline on a waterfront with an observation tower under a blue sky"></div>
<div class="abs call"><svg width="13" height="13" viewBox="0 0 24 24"><path fill="#fff" d="M6.6 10.8a15 15 0 0 0 6.6 6.6l2.2-2.2c.3-.3.7-.4 1-.2 1.1.4 2.3.6 3.6.6.6 0 1 .4 1 1V20c0 .6-.4 1-1 1A17 17 0 0 1 3 4c0-.6.4-1 1-1h3.5c.6 0 1 .4 1 1 0 1.3.2 2.5.6 3.6.1.3 0 .7-.2 1z"/></svg>Call us! 555-010-7890</div>

<div class="abs hero-box">
  <h1 class="serif">VELTRONA</h1>
  <p>Lorem ipsum dolor sit amet, consectetur adipiscing elit, sed do eiusmod tempor incididunt</p>
  <span class="btn-white">GET STARTED</span>
</div>

<h2 class="abs section-title serif" style="top:884px">OUR SERVICES</h2>
<div class="abs card" style="left:112px;top:981px">
  <div class="photo" role="img" aria-label="Agent handing house keys to a couple in a bright kitchen"></div>
  <h3>Real Estate</h3>
  <p>Lorem ipsum dolor sit amet, consectetur adipiscing elit, sed do eiusmod tempor incididunt ut labore et</p>
  <span class="btn-blue">READ MORE <svg width="12" height="12" viewBox="0 0 12 12"><circle cx="6" cy="6" r="6" fill="#fff"/><path d="M4.5 3l3 3-3 3" stroke="#0b5480" stroke-width="1.8" fill="none"/></svg></span>
</div>
<div class="abs card" style="left:445px;top:981px">
  <div class="photo" role="img" aria-label="Two colleagues reviewing data on tablets in an office"></div>
  <h3>Wealth Management</h3>
  <p>Lorem ipsum dolor sit amet, consectetur adipiscing elit, sed do eiusmod tempor incididunt ut labore et</p>
  <span class="btn-blue">READ MORE <svg width="12" height="12" viewBox="0 0 12 12"><circle cx="6" cy="6" r="6" fill="#fff"/><path d="M4.5 3l3 3-3 3" stroke="#0b5480" stroke-width="1.8" fill="none"/></svg></span>
</div>
<div class="abs card" style="left:779px;top:981px">
  <div class="photo" role="img" aria-label="Consultant meeting with a client at a desk with a laptop"></div>
  <h3>Consulting</h3>
  <p>Lorem ipsum dolor sit amet, consectetur adipiscing elit, sed do eiusmod tempor incididunt ut labore et</p>
  <span class="btn-blue">READ MORE <svg width="12" height="12" viewBox="0 0 12 12"><circle cx="6" cy="6" r="6" fill="#fff"/><path d="M4.5 3l3 3-3 3" stroke="#0b5480" stroke-width="1.8" fill="none"/></svg></span>
</div>

<section class="abs about">
  <div class="abs about-panel"></div>
  <div class="abs about-photo" role="img" aria-label="Three business people talking in an office, one holding a clipboard"></div>
  <h2 class="abs serif">ABOUT US</h2>
  <p class="abs" style="top:128px">Sed ut perspiciatis unde omnis iste natus error sit voluptatem accusantium doloremque laudantium, totam rem aperiam, eaque ipsa quae ab illo inventore veritatis et quasi architecto beatae vitae dicta sunt explicabo. Nemo enim ipsam voluptatem</p>
  <p class="abs" style="top:240px">Sed ut perspiciatis unde omnis iste natus error sit voluptatem accusantium doloremque laudantium,</p>
  <span class="btn-white">READ MORE <svg width="12" height="12" viewBox="0 0 12 12"><circle cx="6" cy="6" r="6" fill="#0b5480"/><path d="M4.5 3l3 3-3 3" stroke="#fff" stroke-width="1.8" fill="none"/></svg></span>
</section>

<h2 class="abs section-title serif" style="top:2040px">WHY CHOOSE US</h2>
<div class="abs why-col" style="left:99px;top:2151px">
  <svg width="80" height="72" viewBox="0 0 80 72" fill="none" stroke="#0b5480" stroke-width="2.4"><path d="M8 38L32 18l24 20"/><path d="M14 34v30h36V34"/><rect x="26" y="46" width="12" height="18"/><path d="M4 66h72"/><text x="58" y="20" fill="#0b5480" stroke="none" font-size="22" font-family="Roboto,sans-serif" font-weight="700">$</text></svg>
  <h4>Lorem ipsum dolor sit amet</h4>
  <p>Sed ut perspiciatis unde omnis iste natus error sit voluptatem accusantium doloremque laudantium, totam rem aperiam,</p>
</div>
<div class="abs why-col" style="left:439px;top:2151px">
  <svg width="80" height="72" viewBox="0 0 80 72" fill="none" stroke="#0b5480" stroke-width="2.4"><rect x="12" y="6" width="56" height="42" rx="3"/><circle cx="40" cy="27" r="9"/><path d="M8 58l14-8h14l8 6-8 6H24"/><path d="M72 58l-14-8"/></svg>
  <h4>Lorem ipsum dolor sit amet</h4>
  <p>Sed ut perspiciatis unde omnis iste natus error sit voluptatem accusantium doloremque laudantium, totam rem aperiam,</p>
</div>
<div class="abs why-col" style="left:777px;top:2151px">
  <svg width="80" height="72" viewBox="0 0 80 72" fill="none" stroke="#0b5480" stroke-width="2.4"><rect x="30" y="4" width="36" height="48" rx="2"/><path d="M38 16h20M38 24h20M38 32h12"/><rect x="10" y="26" width="24" height="40" rx="4"/><circle cx="22" cy="38" r="6"/><path d="M15 52h14M15 58h14"/></svg>
  <h4>Lorem ipsum dolor sit amet</h4>
  <p>Sed ut perspiciatis unde omnis iste natus error sit voluptatem accusantium doloremque laudantium, totam rem aperiam,</p>
</div>

<section class="abs clients">
  <h2 class="abs section-title serif">WHAT OUR CLIENTS THINK</h2>
  <div class="abs quote" style="left:104px;top:134px">
    <svg class="marks" width="54" height="40" viewBox="0 0 54 40"><circle cx="12" cy="12" r="11" fill="#8fb3ca"/><path d="M19 18c0 10-6 18-15 21l-1-4c6-3 9-8 9-14z" fill="#8fb3ca"/><circle cx="40" cy="12" r="11" fill="#8fb3ca"/><path d="M47 18c0 10-6 18-15 21l-1-4c6-3 9-8 9-14z" fill="#8fb3ca"/></svg>
    <p>Lorem ipsum dolor sit amet, consectetur<br>adipiscing elit, sed do eiusmod tempor<br>incididunt ut labore dolore magna<br>Ut enim ad minim</p>
    <strong>DL Varga, Norbrook Media</strong>
  </div>
  <div class="abs quote" style="left:444px;top:134px">
    <svg class="marks" width="54" height="40" viewBox="0 0 54 40"><circle cx="12" cy="12" r="11" fill="#8fb3ca"/><path d="M19 18c0 10-6 18-15 21l-1-4c6-3 9-8 9-14z" fill="#8fb3ca"/><circle cx="40" cy="12" r="11" fill="#8fb3ca"/><path d="M47 18c0 10-6 18-15 21l-1-4c6-3 9-8 9-14z" fill="#8fb3ca"/></svg>
    <p>Lorem ipsum dolor sit amet, consectetur<br>adipiscing elit, sed do eiusmod tempor<br>incididunt ut labore dolore magna<br>Ut enim ad minim</p>
    <strong>Kestrel-Arden Motor Team</strong>
  </div>
  <div class="abs quote" style="left:783px;top:134px">
    <svg class="marks" width="54" height="40" viewBox="0 0 54 40"><circle cx="12" cy="12" r="11" fill="#8fb3ca"/><path d="M19 18c0 10-6 18-15 21l-1-4c6-3 9-8 9-14z" fill="#8fb3ca"/><circle cx="40" cy="12" r="11" fill="#8fb3ca"/><path d="M47 18c0 10-6 18-15 21l-1-4c6-3 9-8 9-14z" fill="#8fb3ca"/></svg>
    <p>Lorem ipsum dolor sit amet, consectetur<br>adipiscing elit, sed do eiusmod tempor<br>incididunt ut labore dolore magna<br>Ut enim ad minim</p>
    <strong>Halvern Energy Co.</strong>
  </div>
</section>

<section class="contact">
  <h2 class="abs section-title serif" style="top:2900px">CONTACT US</h2>
  <h3 class="abs" style="left:112px;top:2996px">Contact Details</h3>
  <h3 class="abs" style="left:560px;top:2996px">Get In Touch</h3>
  <div class="abs detail" style="left:112px;top:3050px"><svg width="12" height="18" viewBox="0 0 12 18" style="margin-top:4px"><path fill="#0b5480" d="M6 0a6 6 0 0 1 6 6c0 4.5-6 12-6 12S0 10.5 0 6a6 6 0 0 1 6-6z"/><circle cx="6" cy="6" r="2.2" fill="#fff"/></svg><span>Birchfield Court Offices 482 Harrow Lane<br>Eastmoor, PA 17390</span></div>
  <div class="abs map" role="img" aria-label="Map showing the office location"></div>
  <div class="abs detail" style="left:112px;top:3284px;gap:12px"><svg width="14" height="14" viewBox="0 0 24 24" style="margin-top:4px"><path fill="#0b5480" d="M6.6 10.8a15 15 0 0 0 6.6 6.6l2.2-2.2c.3-.3.7-.4 1-.2 1.1.4 2.3.6 3.6.6.6 0 1 .4 1 1V20c0 .6-.4 1-1 1A17 17 0 0 1 3 4c0-.6.4-1 1-1h3.5c.6 0 1 .4 1 1 0 1.3.2 2.5.6 3.6.1.3 0 .7-.2 1z"/></svg>555.019.4827</div>
  <div class="abs detail" style="left:112px;top:3314px;gap:9px"><svg width="15" height="12" viewBox="0 0 15 12" style="margin-top:6px"><rect width="15" height="12" rx="1" fill="#0b5480"/><path d="M1 1.5l6.5 5 6.5-5" stroke="#fff" stroke-width="1.4" fill="none"/></svg>info@veltrona.com</div>

  <div class="abs field" style="left:560px;top:3056px;width:248px;height:45px"><svg width="11" height="12" viewBox="0 0 11 12" fill="none" stroke="#777" stroke-width="1.2"><circle cx="5.5" cy="3.5" r="2.8"/><path d="M1 11.5c0-3 2-4.5 4.5-4.5s4.5 1.5 4.5 4.5z"/></svg>Name</div>
  <div class="abs field" style="left:839px;top:3056px;width:249px;height:45px"><svg width="11" height="11" viewBox="0 0 24 24"><path fill="#777" d="M6.6 10.8a15 15 0 0 0 6.6 6.6l2.2-2.2c.3-.3.7-.4 1-.2 1.1.4 2.3.6 3.6.6.6 0 1 .4 1 1V20c0 .6-.4 1-1 1A17 17 0 0 1 3 4c0-.6.4-1 1-1h3.5c.6 0 1 .4 1 1 0 1.3.2 2.5.6 3.6.1.3 0 .7-.2 1z"/></svg>Phone Number</div>
  <div class="abs field" style="left:560px;top:3115px;width:248px;height:45px"><svg width="12" height="10" viewBox="0 0 12 10" fill="none" stroke="#777" stroke-width="1.2"><rect x=".6" y=".6" width="10.8" height="8.8" rx="1"/><path d="M1 1.5l5 4 5-4"/></svg>Email Address</div>
  <div class="abs field" style="left:839px;top:3115px;width:249px;height:45px"><svg width="11" height="11" viewBox="0 0 11 11"><path d="M1 10l1-3 6-6 2 2-6 6z" fill="#777"/></svg>Subject</div>
  <div class="abs field" style="left:560px;top:3172px;width:526px;height:85px;align-items:flex-start;padding-top:30px"><svg width="12" height="11" viewBox="0 0 12 11" fill="none" stroke="#777" stroke-width="1.2"><path d="M1 1h10v6H5l-3 3V7H1z"/></svg>Messagge</div>
  <div class="abs submit">SUBMIT</div>
</section>

<footer class="abs site-footer">
  <div class="legal">© 2021 Veltrona &nbsp;|&nbsp; Terms and Conditions &nbsp;|&nbsp; Privacy</div>
  <span class="social" style="left:996px"></span>
  <span class="social" style="left:1028px"></span>
  <span class="social" style="left:1060px"></span>
</footer>

</body>
</html>
```